Can you create a Business Card based on the Logo you designed.

See example and would like to see other examples.

Trying to keep it very clean with a focus on the logo and name.

```html
<!DOCTYPE html>
<html lang="en">
<head>
<meta charset="utf-8">
<title>Fieldrow Business Card</title>
<link href="https://fonts.googleapis.com/css2?family=Montserrat:wght@400;500;700&display=swap" rel="stylesheet">
<style>
  :root {
    --backdrop: #262626;
    --card: #ffffff;
    --green-dark: #117a3c;
    --green-light: #7cc242;
    --sun: #f29a2e;
    --ink: #1f1f1f;
  }
  * { margin: 0; padding: 0; box-sizing: border-box; }
  html, body { width: 1200px; height: 900px; overflow: hidden; }
  body {
    background: var(--backdrop);
    font-family: "Montserrat", sans-serif;
    position: relative;
  }
  .card {
    position: absolute;
    width: 560px;
    height: 320px;
    background: var(--card);
    border-radius: 18px;
    overflow: hidden;
    box-shadow: 0 14px 30px rgba(0,0,0,0.45);
  }
  .card--front { left: 70px; top: 90px; }
  .card--back { left: 570px; top: 480px; }

  .edge-band {
    position: absolute;
    left: 0; right: 0; bottom: 0;
    height: 10px;
    display: flex;
    gap: 6px;
  }
  .edge-band__dark { flex: 0 0 64%; background: var(--green-dark); }
  .edge-band__light { flex: 1; background: var(--green-light); }

  .brand {
    display: flex;
    align-items: center;
    justify-content: center;
    gap: 12px;
    color: var(--green-dark);
    font-weight: 700;
  }
  .brand__dot {
    width: 30px; height: 30px;
    border-radius: 50%;
    background: var(--sun);
  }
  .card--front .brand {
    position: absolute;
    left: 0; right: 0; top: 118px;
    font-size: 58px;
  }
  .card--back .brand {
    position: absolute;
    left: 0; right: 0; top: 46px;
    font-size: 50px;
  }
  .card--back .brand__dot { width: 26px; height: 26px; }

  .details {
    position: absolute;
    top: 150px;
    left: 0; right: 0;
    display: flex;
    justify-content: center;
    align-items: center;
    gap: 20px;
  }
  .person { text-align: right; }
  .person__name {
    color: var(--green-dark);
    font-weight: 700;
    font-size: 22px;
  }
  .person__role {
    color: var(--ink);
    font-size: 12px;
    margin-top: 2px;
  }
  .divider {
    width: 1.5px;
    height: 66px;
    background: var(--green-dark);
  }
  .contacts { list-style: none; }
  .contacts li {
    display: flex;
    align-items: center;
    gap: 8px;
    font-size: 12px;
    color: var(--ink);
    line-height: 20px;
  }
  .contacts svg { width: 12px; height: 12px; fill: var(--green-dark); }

  .address {
    position: absolute;
    left: 0; right: 0; bottom: 42px;
    text-align: center;
    font-size: 12.5px;
    color: var(--ink);
  }
</style>
</head>
<body>

<section class="card card--front">
  <div class="brand"><span class="brand__dot"></span>Fieldrow</div>
  <div class="edge-band"><span class="edge-band__dark"></span><span class="edge-band__light"></span></div>
</section>

<section class="card card--back">
  <div class="brand"><span class="brand__dot"></span>Fieldrow</div>

  <div class="details">
    <div class="person">
      <div class="person__name">Marcus Hale</div>
      <div class="person__role">Chief Executive Officer</div>
    </div>
    <div class="divider"></div>
    <ul class="contacts">
      <li>
        <svg viewBox="0 0 24 24" aria-hidden="true"><path d="M6.6 10.8a15.1 15.1 0 0 0 6.6 6.6l2.2-2.2a1 1 0 0 1 1-.25 11.4 11.4 0 0 0 3.6.57 1 1 0 0 1 1 1V20a1 1 0 0 1-1 1A17 17 0 0 1 3 4a1 1 0 0 1 1-1h3.5a1 1 0 0 1 1 1c0 1.25.2 2.45.57 3.57a1 1 0 0 1-.25 1z"/></svg>
        +1 (555) 214-7788
      </li>
      <li>
        <svg viewBox="0 0 24 24" aria-hidden="true"><path d="M2 5h20v14H2zm2 2v.5l8 5 8-5V7l-8 5z"/></svg>
        ceo@fieldrow.com
      </li>
      <li>
        <svg viewBox="0 0 24 24" aria-hidden="true"><path d="M12 2a10 10 0 1 0 0 20 10 10 0 0 0 0-20zm0 2c.9 0 2.2 2 2.7 5H9.3C9.8 6 11.1 4 12 4zm-7.7 7h3a17 17 0 0 0 0 2h-3a8 8 0 0 1 0-2zm5 0h5.4a15 15 0 0 1 0 2H9.3a15 15 0 0 1 0-2zm7.4 0h3a8 8 0 0 1 0 2h-3a17 17 0 0 0 0-2zM9.3 15h5.4c-.5 3-1.8 5-2.7 5s-2.2-2-2.7-5z"/></svg>
        www.fieldrow.com
      </li>
    </ul>
  </div>

  <p class="address">418 Meadow Lane, #112 Brookfield, OH 43990</p>

  <div class="edge-band"><span class="edge-band__dark"></span><span class="edge-band__light"></span></div>
</section>

</body>
</html>
```